Sunny Paths and joy Business card

I have a logo, but will like a business card design. Is for a travel agency in Mexico. We focus in family experiences.

I will liek some thing different and unique, from the traditional business card, something to get remmeber for.

Business card information:

Leandro T. Ocampo
leandro@sunnypathsjoy.example

Alameda 482, 3 piso
Col. Tlalpizco
Mexico, D.F. 07320

office: (55) 5000-0142
mobile: (55) 9000-0187

www.sunnypathsjoy.example
@sunnypjoy
blog: sunnypathsandjoy.blogsite.example
facebook: SunnyPathsAndJoy

```html
<!DOCTYPE html>
<html lang="es">
<head>
<meta charset="utf-8">
<title>Sunny Paths and joy — Business card</title>
<link href="https://fonts.googleapis.com/css2?family=Arimo:wght@700&family=Carlito:wght@400;700&display=swap" rel="stylesheet">
<style>
  :root {
    --sky: #1aa2e6;
    --sky-deep: #0f86d0;
    --sky-light: #d7eefb;
    --navy: #1f4f9c;
    --paper: #ffffff;
    --panel-edge: #e9e6f5;
  }
  * { margin: 0; padding: 0; box-sizing: border-box; }
  html, body { width: 682px; height: 1200px; overflow: hidden; background: var(--paper); }
  .card { position: relative; width: 682px; height: 1200px; background: var(--paper); font-family: "Carlito", "Calibri", sans-serif; }

  .tag-art { position: absolute; left: 0; top: 0; width: 222px; height: 205px;
    border-radius: 0 0 60px 0;
    background: linear-gradient(135deg, var(--sky-deep), var(--sky) 70%, #bfe3f8); }

  .brand { position: absolute; left: 0; width: 682px; top: 30px; text-align: center; }
  .brand-disc { display: block; width: 170px; height: 170px; margin: 0 auto; border-radius: 50%;
    background: radial-gradient(circle at 50% 45%, var(--sky-light), #a9d7f3); }
  .brand-name { margin-top: 14px; font-family: "Arimo", Arial, sans-serif; font-weight: 700;
    font-size: 44px; line-height: 50px; color: var(--navy); }

  .frame { position: absolute; left: 29px; top: 349px; width: 626px; height: 829px; border-radius: 52px;
    background: linear-gradient(180deg, #2fb0ee, var(--sky-deep)); box-shadow: 0 2px 6px rgba(0,0,0,.12); }
  .frame-stitch { position: absolute; left: 16px; top: 16px; right: 16px; bottom: 16px;
    border: 3px dashed var(--paper); border-radius: 42px; }

  .panel { position: absolute; left: 91px; top: 414px; width: 501px; height: 705px; border-radius: 30px;
    background: linear-gradient(180deg, var(--paper) 80%, var(--panel-edge)); }

  .holder-name { position: absolute; left: 0; width: 100%; top: 22px; text-align: center;
    font-family: "Arimo", Arial, sans-serif; font-weight: 700; font-size: 30px; color: var(--navy); }

  .address { position: absolute; left: 54px; top: 80px; width: 395px; height: 242px; border-radius: 26px;
    background: var(--sky); padding: 16px 0 0 36px; color: var(--paper); font-size: 28px; line-height: 43.5px; font-style: normal; }

  .contacts { position: absolute; left: 16px; top: 342px; width: 480px; list-style: none; color: var(--navy); font-size: 28px; }
  .contact { display: flex; align-items: center; height: 66px; }
  .contact-icon { flex: 0 0 52px; width: 52px; height: 52px; margin-right: 10px; }
  .contact-blog { display: block; height: auto; margin-top: 2px; }
  .contact-blog .row { display: flex; align-items: center; }
  .contact-blog .url { display: block; line-height: 34px; }
</style>
</head>
<body>
<main class="card">
  <div class="tag-art" role="img" aria-label="Decorative blue luggage tag illustration"></div>

  <header class="brand">
    <span class="brand-disc" role="img" aria-label="Logo illustration area: cartoon airplane among clouds"></span>
    <p class="brand-name">Sunny Paths and joy</p>
  </header>

  <div class="frame"><div class="frame-stitch"></div></div>

  <section class="panel">
    <h1 class="holder-name">Leandro T. Ocampo</h1>
    <address class="address">
      Alameda 482, 3 piso<br>
      Col. Tlalpizco<br>
      Mexico, D.F. 07320<br>
      Office: (55) 5000-0142<br>
      Mobile: (55) 9000-0187
    </address>

    <ul class="contacts">
      <li class="contact">
        <svg class="contact-icon" viewBox="0 0 52 52" aria-hidden="true">
          <circle cx="26" cy="26" r="24" fill="var(--sky)"/>
          <circle cx="26" cy="26" r="14" fill="none" stroke="var(--paper)" stroke-width="2.5"/>
          <ellipse cx="26" cy="26" rx="6" ry="14" fill="none" stroke="var(--paper)" stroke-width="2"/>
          <line x1="12" y1="26" x2="40" y2="26" stroke="var(--paper)" stroke-width="2"/>
        </svg>
        <span>www.sunnypathsjoy.example</span>
      </li>
      <li class="contact">
        <svg class="contact-icon" viewBox="0 0 52 52" aria-hidden="true">
          <circle cx="26" cy="26" r="24" fill="var(--sky)"/>
          <rect x="13" y="17" width="26" height="18" rx="2" fill="var(--paper)"/>
          <polyline points="13,18 26,28 39,18" fill="none" stroke="var(--sky)" stroke-width="2"/>
        </svg>
        <span>leandro@sunnypathsjoy.example</span>
      </li>
      <li class="contact">
        <svg class="contact-icon" viewBox="0 0 52 52" aria-hidden="true">
          <rect x="4" y="4" width="44" height="44" rx="3" fill="var(--navy)"/>
        </svg>
        <span>SunnyPathsAndJoy</span>
      </li>
      <li class="contact">
        <svg class="contact-icon" viewBox="0 0 52 52" aria-hidden="true">
          <circle cx="26" cy="26" r="22" fill="var(--sky)"/>
        </svg>
        <span>@sunnypjoy</span>
      </li>
      <li class="contact contact-blog">
        <div class="row">
          <svg class="contact-icon" viewBox="0 0 52 52" aria-hidden="true">
            <circle cx="26" cy="26" r="22" fill="var(--sky)"/>
          </svg>
          <span>Blog:</span>
        </div>
        <span class="url">sunnypathsandjoy.blogsite.example</span>
      </li>
    </ul>
  </section>
</main>
</body>
</html>
```